Modern Homepage Design for brenvik.nl – Fish & Chicken Food Webshop

Brenvik.nl is an online store that sells fish and chicken food. The design should be visually appealing, easy to navigate, and optimized for e-commerce. We want a layout that helps customers quickly find what they need and encourages them to explore our products.
A good example of the style and structure we like is dierkamp.nl – clean layout, clear product focus, and user-friendly navigation.
Brand Colors (must be used):
Orange: #f7a441
Dark Gray: #3c3c3b
White: #ffffff
Please use these colors consistently throughout the design.
Homepage Requirements:
The homepage should include the following sections:
Main Slider / Hero Banner
A large, eye-catching slider at the top of the page to highlight promotions or featured categories.
Category Blocks
A section with clear, clickable blocks or tiles that link to main product categories (e.g., Fish Food, Chicken Food, Accessories).
Featured Products
A section showcasing selected or best-selling products.
Special Offers / Promotions
A space to highlight current deals or limited-time offers.
Three Banners in a Row
A section with three horizontal banners side by side, which can be used for promotions, shipping info, or other key messages.
Unique Selling Points (USPs)
A section that briefly explains what makes our store different (e.g., fast delivery, high-quality feed, trusted by professionals).
SEO Content Block
A short paragraph of text for SEO purposes (use Lorem Ipsum for dummy content).
Footer Design
Include space for contact information, navigation links, and social media.
Design Notes:
The design must be responsive and mobile-friendly.
Focus on clean layout, good spacing, and easy navigation.
Use modern fonts and a clear visual hierarchy.
We are only looking for the homepage design at this stage, but we may work with the selected designer on additional pages later.
Deliverables:
Homepage design in layered PSD, Figma, or Adobe XD format
Any fonts and assets used
Preview images/mockups
We look forward to seeing your ideas and working with a designer who can bring our brand to life with a fresh and functional homepage design.
Let us know if you have any questions.
Hobby Animal Keepers, Pet Owners
Animal Nutrition & Feed
2 page

```html
<!DOCTYPE html>
<html lang="en">
<head>
<meta charset="utf-8">
<title>Brenvik.nl – Fish &amp; Chicken Food</title>
<link href="https://fonts.googleapis.com/css2?family=Lilita+One&family=Montserrat:wght@400;500;600;700&display=swap" rel="stylesheet">
<style>
:root{
  --orange:#f7a441;
  --orange-deep:#ef8f2a;
  --dark:#3c3c3b;
  --white:#ffffff;
  --text:#555554;
  --muted:#8a8a88;
  --cream:#fdf1e2;
  --line:#e4e4e2;
}
*{box-sizing:border-box;margin:0;padding:0}
html,body{width:1200px;height:4124px;overflow:hidden}
body{position:relative;background:var(--white);font-family:'Montserrat',sans-serif;color:var(--text)}
.abs{position:absolute}
.display{font-family:'Lilita One',cursive;color:var(--dark);font-weight:400}
a{color:inherit;text-decoration:none}

.topbar{left:0;top:0;width:1200px;height:34px;background:var(--orange);color:var(--white);font-size:14px;display:flex;justify-content:center;align-items:center;gap:28px}
.header{left:0;top:34px;width:1200px;height:92px;background:var(--white);display:flex;align-items:center}
.brand{display:flex;align-items:center;gap:10px;font-family:'Montserrat',sans-serif;font-weight:700;color:var(--dark)}
.brand .dot{border-radius:50%;background:var(--orange)}
.header .brand{position:absolute;left:90px;font-size:44px}
.header .brand .dot{width:40px;height:40px}
.nav{position:absolute;left:414px;display:flex;gap:34px;font-size:14px;font-weight:500;color:var(--dark);align-items:center}
.search{position:absolute;left:1054px;top:18px;width:56px;height:56px;border-radius:50%;background:#e9e9e9;display:flex;align-items:center;justify-content:center}

.hero{left:0;top:126px;width:1200px;height:786px;background:linear-gradient(180deg,#4a5a2c 0%,#8a6b2a 35%,#7a4a22 60%,#6e8a2a 88%,#e48f34 100%)}
.hero-title{left:0;top:100px;width:1200px;text-align:center;color:var(--white);font-size:72px;line-height:74px}
.hero-sub{left:0;top:248px;width:1200px;text-align:center;color:var(--white);font-size:14px}
.btn{display:flex;align-items:center;justify-content:center;background:var(--orange);color:var(--white);font-weight:600;border-radius:30px}
.hero .btn{left:480px;top:286px;width:240px;height:48px;font-size:16px}
.slide-arrow{width:76px;height:76px;border-radius:50%;background:rgba(30,30,30,.8);display:flex;align-items:center;justify-content:center;top:303px}

.about-band{left:0;top:912px;width:1200px;height:499px;background:var(--orange)}
.about-photo{left:154px;top:125px;width:472px;height:315px;border-radius:30px;border:3px solid var(--white);background:linear-gradient(160deg,#1f8fb0,#3cb6c9 45%,#d36a2a 75%,#1d5b6e)}
.about-title{left:674px;top:173px;color:var(--white);font-size:46px}
.about-text{left:674px;top:234px;width:380px;color:var(--white);font-size:14px;line-height:22px}
.about-link{left:674px;top:363px;color:var(--white);font-size:15px;font-weight:600;border-bottom:2px solid var(--white);padding-bottom:3px}

.section-title{left:0;width:1200px;text-align:center;font-size:44px}
.cat-card{top:1571px;width:456px;height:170px;border-radius:18px;background:linear-gradient(135deg,#fff 60%,#f4f4f4);box-shadow:0 4px 18px rgba(0,0,0,.1)}
.cat-card h3{position:absolute;left:32px;top:34px;font-size:22px}
.cat-card p{position:absolute;left:32px;top:68px;width:280px;font-size:14px;line-height:22px;color:var(--muted)}
.cat-card .shop{position:absolute;left:32px;top:114px;font-size:14px;font-weight:600;color:var(--orange);border-bottom:2px solid var(--orange);padding-bottom:2px}
.cat-card .thumb{position:absolute;right:30px;top:22px;width:120px;height:120px;border-radius:50%}
.circle-arrow{width:44px;height:44px;border-radius:50%;display:flex;align-items:center;justify-content:center;top:1640px}

.why-title{left:144px;top:1908px;font-size:46px}
.why-list{left:144px;top:1978px;list-style:none;font-size:14px;color:var(--text)}
.why-list li{display:flex;align-items:center;gap:14px;height:32px}
.tick{width:13px;height:13px;border-radius:50%;background:var(--orange);flex:none;display:flex;align-items:center;justify-content:center}
.why .btn{left:144px;top:2155px;width:286px;height:45px;font-size:14px}
.why-big{left:651px;top:1849px;width:404px;height:404px;border-radius:50%;background:radial-gradient(circle at 45% 45%,#8fa7a8,#3e6a32 55%,#1f3a1a)}
.why-small{left:622px;top:2104px;width:164px;height:164px;border-radius:50%;border:4px solid var(--white);background:radial-gradient(circle at 50% 45%,#7a3a1c,#3a4a20 60%,#6a8a3a)}

.trio-col{width:352px;text-align:center}
.trio-icon{width:78px;height:78px;border-radius:50%;background:var(--orange);margin:0 auto;display:flex;align-items:center;justify-content:center}
.trio-col h4{font-family:'Lilita One',cursive;color:var(--dark);font-weight:400;font-size:21px;margin-top:20px}
.trio-col p{font-size:14px;color:var(--muted);margin-top:6px}
.divider{width:2px;background:var(--line)}

.fav-card{top:2797px;width:293px;height:310px;border-radius:20px;background:var(--cream);text-align:center}
.fav-card .img{margin:11px auto 0;width:268px;height:173px;border-radius:16px}
.fav-card h4{font-family:'Lilita One',cursive;font-weight:400;color:var(--dark);font-size:22px;line-height:27px;margin-top:18px}
.fav-card .price{font-size:22px;font-weight:600;color:var(--orange);margin-top:10px}

.deal-col{width:352px;text-align:center}
.deal-col p{font-size:14px;color:var(--text);line-height:22px;margin-top:26px}

.footer{left:0;top:3712px;width:1200px;height:412px;background:var(--dark);color:var(--white)}
.footer .brand{position:absolute;left:480px;top:64px;font-size:64px;color:var(--white);gap:14px}
.footer .brand .dot{width:56px;height:56px}
.fcol{top:168px}
.fcol h5{font-family:'Lilita One',cursive;font-weight:400;font-size:21px;color:var(--white);margin-bottom:12px}
.fcol li{list-style:none;font-size:13px;line-height:26.6px;color:#e9e9e9;display:flex;gap:10px;align-items:flex-start}
.fcol li svg{flex:none;margin-top:7px}
.frule{left:88px;top:354px;width:1024px;height:1px;background:#6a6a69}
.copy{left:0;top:376px;width:1200px;text-align:center;font-size:13px;color:#e9e9e9}
.chat{left:1075px;top:315px;width:70px;height:70px;border-radius:50%;background:var(--orange);display:flex;align-items:center;justify-content:center}
</style>
</head>
<body>

<div class="abs topbar"><span>Free Shipping on Orders Over €49</span><span>|</span><span>Fast Delivery Across the Netherlands</span></div>

<header class="abs header">
  <a class="brand"><span class="dot"></span>brenvik</a>
  <nav class="nav">
    <svg width="16" height="14" viewBox="0 0 16 14"><path d="M8 0L0 7h2v7h4V9h4v5h4V7h2z" fill="#f7a441"/></svg>
    <a>Fish Food</a><a>Chicken Food</a><a>Accessories</a><a>About Us</a><a>Blog</a><a>Contact</a>
  </nav>
  <div class="search"><svg width="18" height="18" viewBox="0 0 18 18"><circle cx="7.5" cy="7.5" r="5.5" fill="none" stroke="#3c3c3b" stroke-width="2"/><path d="M12 12l4.5 4.5" stroke="#3c3c3b" stroke-width="2"/></svg></div>
</header>

<section class="abs hero" role="img" aria-label="Row of five hens standing on green grass in front of a blurred autumn meadow">
  <h1 class="abs display hero-title" style="color:#fff">Feed Your Fish the Best<br>Every Time!</h1>
  <p class="abs hero-sub">Discover premium fish food trusted by hobbyists and professionals.</p>
  <a class="abs btn">Shop Fish Food</a>
  <div class="abs slide-arrow" style="left:50px"><svg width="14" height="14" viewBox="0 0 14 14"><path d="M9 2L4 7l5 5" fill="none" stroke="#fff" stroke-width="2.5"/></svg></div>
  <div class="abs slide-arrow" style="left:1072px"><svg width="14" height="14" viewBox="0 0 14 14"><path d="M5 2l5 5-5 5" fill="none" stroke="#fff" stroke-width="2.5"/></svg></div>
</section>

<section class="abs about-band">
  <div class="abs about-photo" role="img" aria-label="Colourful tropical fish swimming over coral reef"></div>
  <h2 class="abs display about-title" style="color:#fff">About Us</h2>
  <p class="abs about-text">At Brenvik.nl, we're passionate about providing the very best feed for fish and poultry. Since 1998, we've been committed to delivering top-quality nutrition that ensures healthy growth, strong immunity, and vibrant life for your animals.</p>
  <a class="abs about-link">Learn More About Us</a>
</section>

<h2 class="abs display section-title" style="top:1492px">Shop By Category</h2>
<div class="abs circle-arrow" style="left:61px;background:#9a9a98"><svg width="10" height="10" viewBox="0 0 10 10"><path d="M6.5 1.5L3 5l3.5 3.5" fill="none" stroke="#fff" stroke-width="1.6"/></svg></div>
<article class="abs cat-card" style="left:131px">
  <h3 class="display">Fish Food</h3>
  <p>Complete nutrition for tropical, pond, and aquarium fish.</p>
  <a class="shop">Shop Now</a>
  <div class="thumb" role="img" aria-label="Glass jar of fish food pellets" style="background:radial-gradient(circle,#c9b79a,#e8e1d4 70%,#fff)"></div>
</article>
<article class="abs cat-card" style="left:611px">
  <h3 class="display">Chicken Food</h3>
  <p>Balanced feed for laying hens, broilers, and chicks.</p>
  <a class="shop">Shop Now</a>
  <div class="thumb" role="img" aria-label="Burlap sack spilling chicken feed pellets" style="background:radial-gradient(circle,#c9924a,#ead3ac 70%,#fff)"></div>
</article>
<div class="abs circle-arrow" style="left:1095px;background:var(--orange)"><svg width="10" height="10" viewBox="0 0 10 10"><path d="M3.5 1.5L7 5 3.5 8.5" fill="none" stroke="#fff" stroke-width="1.6"/></svg></div>

<section class="why">
  <h2 class="abs display why-title">Why Choose Us</h2>
  <ul class="abs why-list">
    <li><span class="tick"><svg width="7" height="7" viewBox="0 0 7 7"><path d="M1 3.5l1.7 1.7L6 1.8" fill="none" stroke="#fff" stroke-width="1.3"/></svg></span>Over 25 years of experience in animal nutrition.</li>
    <li><span class="tick"><svg width="7" height="7" viewBox="0 0 7 7"><path d="M1 3.5l1.7 1.7L6 1.8" fill="none" stroke="#fff" stroke-width="1.3"/></svg></span>Trusted by farms, breeders, and hobbyists.</li>
    <li><span class="tick"><svg width="7" height="7" viewBox="0 0 7 7"><path d="M1 3.5l1.7 1.7L6 1.8" fill="none" stroke="#fff" stroke-width="1.3"/></svg></span>Carefully selected, premium-quality ingredients.</li>
    <li><span class="tick"><svg width="7" height="7" viewBox="0 0 7 7"><path d="M1 3.5l1.7 1.7L6 1.8" fill="none" stroke="#fff" stroke-width="1.3"/></svg></span>Fast and reliable nationwide delivery.</li>
    <li><span class="tick"><svg width="7" height="7" viewBox="0 0 7 7"><path d="M1 3.5l1.7 1.7L6 1.8" fill="none" stroke="#fff" stroke-width="1.3"/></svg></span>Excellent customer support.</li>
  </ul>
  <a class="abs btn">Discover the Brenvik Difference</a>
  <div class="abs why-big" role="img" aria-label="Silver angelfish among aquarium plants"></div>
  <div class="abs why-small" role="img" aria-label="Rooster standing on grass"></div>
</section>

<h2 class="abs display section-title" style="top:2370px">Three Banners in a Row</h2>
<div class="abs trio-col" style="left:72px;top:2460px">
  <div class="trio-icon"><svg width="40" height="28" viewBox="0 0 40 28"><rect x="2" y="4" width="22" height="16" rx="2" fill="#fff"/><path d="M24 9h8l5 6v5H24z" fill="#fff"/><circle cx="10" cy="22" r="4" fill="#fff" stroke="#f7a441" stroke-width="2"/><circle cx="30" cy="22" r="4" fill="#fff" stroke="#f7a441" stroke-width="2"/></svg></div>
  <h4>Fast Delivery</h4><p>Across the Netherlands</p>
</div>
<div class="abs divider" style="left:408px;top:2451px;height:160px"></div>
<div class="abs trio-col" style="left:424px;top:2460px">
  <div class="trio-icon"><svg width="32" height="32" viewBox="0 0 32 32"><path d="M16 9c-6-4-12 0-11 8 1 7 6 12 11 10 5 2 10-3 11-10 1-8-5-12-11-8z" fill="#fff"/><path d="M16 9c0-3 2-6 5-7" stroke="#fff" stroke-width="2" fill="none"/></svg></div>
  <h4>High-Quality Nutrition</h4><p>For Fish &amp; Poultry</p>
</div>
<div class="abs divider" style="left:792px;top:2451px;height:160px"></div>
<div class="abs trio-col" style="left:776px;top:2460px">
  <div class="trio-icon"><svg width="36" height="28" viewBox="0 0 36 28"><rect x="2" y="4" width="30" height="20" rx="3" fill="#fff"/><rect x="2" y="9" width="30" height="4" fill="#f7a441"/><rect x="6" y="17" width="10" height="3" fill="#f7a441"/></svg></div>
  <h4>Secure Payments</h4><p>Shop with Confidence</p>
</div>

<h2 class="abs display section-title" style="top:2712px">Customer Favorites</h2>
<article class="abs fav-card" style="left:141px">
  <div class="img" role="img" aria-label="Orange bowl tipped over a pile of goldfish pellets" style="background:linear-gradient(180deg,#7d8593 0%,#8a8c96 55%,#b3703f 80%,#9b5a30)"></div>
  <h4>Premium Goldfish<br>Pellets</h4><div class="price">€8.99</div>
</article>
<article class="abs fav-card" style="left:453px">
  <div class="img" role="img" aria-label="Yellow bowl tipped over layer feed pellets" style="background:linear-gradient(180deg,#7d8593 0%,#8a8c96 55%,#a87446 80%,#8e5b35)"></div>
  <h4>Organic Layer<br>Feed</h4><div class="price">€12.50</div>
</article>
<article class="abs fav-card" style="left:765px">
  <div class="img" role="img" aria-label="Glass jar spilling chick starter crumbs" style="background:linear-gradient(135deg,#2d2b2a,#c9a26a 45%,#d8b27a 60%,#5a2a22)"></div>
  <h4>Chick Starter<br>Crumbs</h4><div class="price">€9.75</div>
</article>
<a class="abs btn" style="left:501px;top:3149px;width:198px;height:45px;font-size:14px">View All Products</a>

<h2 class="abs display section-title" style="top:3290px">This Week's Special Deals</h2>
<div class="abs deal-col" style="left:72px;top:3374px">
  <div class="trio-icon"><svg width="30" height="30" viewBox="0 0 30 30"><rect x="6" y="4" width="18" height="22" rx="2" fill="#fff"/><path d="M10 10h10M10 15h10M10 20h6" stroke="#f7a441" stroke-width="2"/></svg></div>
  <p>Buy 2 Get 1 Free – Chicken<br>Feed Range!</p>
</div>
<div class="abs divider" style="left:408px;top:3365px;height:162px"></div>
<div class="abs deal-col" style="left:424px;top:3374px">
  <div class="trio-icon"><svg width="30" height="30" viewBox="0 0 30 30"><circle cx="15" cy="16" r="11" fill="none" stroke="#fff" stroke-width="3"/><path d="M15 10v6l4 3" stroke="#fff" stroke-width="2.5" fill="none"/></svg></div>
  <p>10% Off All Pond Food –<br>Limited Time Only!</p>
</div>
<div class="abs divider" style="left:792px;top:3365px;height:162px"></div>
<div class="abs deal-col" style="left:776px;top:3374px">
  <div class="trio-icon"><svg width="40" height="28" viewBox="0 0 40 28"><rect x="2" y="4" width="22" height="16" rx="2" fill="#fff"/><path d="M24 9h8l5 6v5H24z" fill="#fff"/><circle cx="10" cy="22" r="4" fill="#fff" stroke="#f7a441" stroke-width="2"/><circle cx="30" cy="22" r="4" fill="#fff" stroke="#f7a441" stroke-width="2"/></svg></div>
  <p>Free Shipping on Orders<br>Above €49!</p>
</div>
<a class="abs btn" style="left:512px;top:3552px;width:176px;height:45px;font-size:14px">Shop Offers</a>

<footer class="abs footer">
  <a class="brand"><span class="dot"></span>brenvik</a>
  <div class="abs fcol" style="left:88px">
    <h5>Stay Connected</h5>
    <ul>
      <li><svg width="11" height="11" viewBox="0 0 12 12"><path d="M2 1l2.5 0 1 3-1.5 1c.7 1.5 1.8 2.6 3 3l1-1.5 3 1V11c-5 0-9-4-9-10z" fill="#f7a441"/></svg>+31 20 555 0148</li>
      <li style="line-height:20px;margin:3px 0"><svg width="11" height="13" viewBox="0 0 11 13" style="margin-top:3px"><path d="M5.5 0A4.5 4.5 0 001 4.5C1 8 5.5 13 5.5 13S10 8 10 4.5A4.5 4.5 0 005.5 0z" fill="#f7a441"/><circle cx="5.5" cy="4.5" r="1.6" fill="#3c3c3b"/></svg>Brenvik B.V., Amsterdam, The<br>Netherlands</li>
      <li><svg width="12" height="10" viewBox="0 0 12 10"><rect width="12" height="10" rx="1" fill="#f7a441"/><path d="M0 1l6 4.5L12 1" stroke="#3c3c3b" fill="none"/></svg>info@brenvik.nl</li>
    </ul>
  </div>
  <div class="abs fcol" style="left:389px">
    <h5>Customer Service</h5>
    <ul><li>Shipping &amp; Delivery</li><li>Returns &amp; Refunds</li><li>Payment Options</li><li>Contact Us</li></ul>
  </div>
  <div class="abs fcol" style="left:698px">
    <h5>About Brenvik.nl</h5>
    <ul><li>Our Story</li><li>Sustainability</li><li>Careers</li><li>Blog</li></ul>
  </div>
  <div class="abs fcol" style="left:986px">
    <h5>My Account</h5>
    <ul><li>Login / Register</li><li>Order History</li><li>Wishlist</li></ul>
  </div>
  <div class="abs frule"></div>
  <p class="abs copy">© 2025 Brenvik.nl — All Rights Reserved</p>
  <div class="abs chat"><svg width="34" height="30" viewBox="0 0 34 30"><path d="M17 2C8.7 2 2 7.6 2 14.5c0 3.5 1.7 6.6 4.5 8.9L5 28l6-3c1.9.6 3.9 1 6 1 8.3 0 15-5.6 15-12.5S25.3 2 17 2z" fill="#fff"/><circle cx="11" cy="14.5" r="2" fill="#f7a441"/><circle cx="17" cy="14.5" r="2" fill="#f7a441"/><circle cx="23" cy="14.5" r="2" fill="#f7a441"/></svg></div>
</footer>

</body>
</html>
```